Boutique startup consulting

Hello,
Me and my partner are starting a boutique consulting/ "venturing for startup" firm and want to make professional looking slides. The point of these slide are to attract Automakers's venture arms to collaborate with us. We are hoping to win clients with this presentation.

Acceptance criteria:
1. You put beautiful designs where-ever you can and make the attached slides look professional. Full freedom in designing the slides. You are the artist, please create some magic
2. The style should be innovative and state of the art. It should be with colourful designs
3. The slides should be very professional
4. We are unsure of how to present our previous experience. Please help us out
5. The first slide has gray background. you may use the original colored image and tweak it

Here is out website:
https://www.plumridge-advisors.net/

Can you please ensure that the slides are presented in the following format?

PRESENTATION
1. Starting Masterslide
2. Customized Starting Masterslide (with Topic + Customer Logo, for eg. Smart City & KLO)
3. Service Categories Masterslide /Overview ( we have 5 Categories which are shown by icon and buzzword, see https://www.plumridge-advisors.net/live/research-strategy/research-strategy.aspx, this is for eg. the Overview for the categorie “Research &Strategy”. We have 2-4 Icon per Category, other categories are Business Development,Venture Building, Expansion Advisory, Sustainable Due Diligence , see webside)
4. Subcategories & Description Masterslide
o We have 15 Subcategories, the Masterslide should just show the Icon and then 1-2 square for description with bullets, f.ex. https://www.plumridge-advisors.net/live/expansion-advisory-feasibility-analysis/feasibility-analysis.aspx
5. Team Presenting Masterslide
o Not like Website, a Masterslide where each Teammember can present him self, in bullets with Education/Business Experience/ other awards/distinction AND in Text bubbles like “Experiences and hands-on Business developer”
6. Contact ( closing Chart with contact data, liked in etc.)
7. Masterslide (free for individual content)
o Just a slide with the CI framework which can be used as Masterslide for other charts like

8. PROPOSAL Masterslide (like customized starting slide, but Proposal)
9. Background Masterslide (Text)
o A textual description
10. Value Proposition & Goals Masterslide (Text & Bullets)
o V P will be textual so for eg. text frame; Goals with 2-4 squares (text/Bullets) for sub-goals and including the tasks for these goals in bullets
11. Milestones & Timing Masterslide (Timeline , Squares & text)
o Timeline, for eg. 6 Month project, where we have 8 tasks with starting and ending
12. Free MAsterslide /Proposal
o Where we can add charts to the proposal like Conditions or Contact

To Add:
- Logo colour description
- Picture and Icons ( so they don’t need to buy new pics or look for them)

Requirements
Must have
• Please check out the slides and make them presentable

```html
<!DOCTYPE html>
<html lang="en">
<head>
<meta charset="utf-8">
<title>Dark Captioned Graphic</title>
<link href="https://fonts.googleapis.com/css2?family=Cabin:wght@400;500;600;700&family=Raleway:wght@400;500;700;800&display=swap" rel="stylesheet">
<style>
  :root {
    --bg: #171717;
    --green: #95bd3a;
    --green-dim: #7f9a3c;
    --white: #f2f2f2;
    --grey: #d9d9d9;
    --grid: #4a4a4a;
    --band: #3b3b3b;
    --divider: #4d5a2c;
  }
  * { margin: 0; padding: 0; box-sizing: border-box; }
  html, body { width: 1200px; height: 675px; overflow: hidden; background: var(--bg); }
  .slide { position: relative; width: 1200px; height: 675px; background: var(--bg); color: var(--white); font-family: "Raleway", sans-serif; overflow: hidden; }

  .title { position: absolute; left: 120px; top: 54px; font-family: "Cabin", sans-serif; font-weight: 600; font-size: 27px; line-height: 33px; color: var(--white); }

  .legend-item { position: absolute; left: 120px; width: 260px; height: 52px; }
  .legend-item .swatch { position: absolute; left: 0; top: 0; width: 10px; height: 52px; }
  .legend-item p { position: absolute; left: 23px; top: 5px; font-family: "Cabin", sans-serif; font-size: 17px; line-height: 21px; white-space: nowrap; }
  .legend-green { top: 189px; }
  .legend-green .swatch { background: var(--green-dim); }
  .legend-green p { color: var(--green); }
  .legend-white { top: 266px; }
  .legend-white .swatch { background: var(--grey); }
  .legend-white p { color: var(--white); }

  .kpi-icon { position: absolute; left: 114px; top: 363px; }
  .kpi-value { position: absolute; left: 183px; top: 360px; font-family: "Cabin", sans-serif; font-weight: 700; font-size: 32px; line-height: 36px; color: var(--green); }
  .kpi-note { position: absolute; left: 183px; top: 395px; font-size: 10.5px; line-height: 13px; color: var(--green); }

  .breadcrumb-bar { position: absolute; left: 547px; top: 67px; width: 225px; height: 7px; background: var(--green); }
  .breadcrumb { position: absolute; left: 781px; top: 64px; font-family: "Cabin", sans-serif; font-weight: 500; font-size: 10px; letter-spacing: 1.1px; color: var(--white); white-space: nowrap; }

  .chart { position: absolute; left: 0; top: 0; width: 1200px; height: 675px; }
  .chart text { font-family: "Raleway", sans-serif; font-size: 15.5px; fill: var(--grey); }

  .divider { position: absolute; left: 0; top: 495px; width: 1200px; height: 1px; background: var(--divider); }

  .stat { position: absolute; top: 522px; width: 270px; height: 70px; }
  .stat .figure { position: absolute; left: 0; top: 0; width: 42px; text-align: center; font-family: "Raleway", sans-serif; font-weight: 800; font-size: 24px; line-height: 26px; color: var(--white); white-space: nowrap; }
  .stat .badge { position: absolute; left: 2px; top: 27px; width: 38px; height: 40px; background: var(--green); border-radius: 3px 3px 9px 9px; display: flex; align-items: center; justify-content: center; }
  .stat .rule { position: absolute; left: 49px; top: 5px; height: 62px; border-left: 1px dashed var(--green); }
  .stat p { position: absolute; left: 58px; top: 0; font-size: 13.6px; line-height: 17px; color: var(--white); white-space: nowrap; }

  .footer-num { position: absolute; left: 0; top: 632px; width: 60px; height: 27px; background: var(--green); font-family: "Cabin", sans-serif; font-weight: 700; font-size: 18px; line-height: 27px; color: var(--white); text-align: right; padding-right: 9px; }
  .footer-band { position: absolute; left: 60px; top: 632px; width: 598px; height: 27px; background: var(--band); font-family: "Cabin", sans-serif; font-size: 15.5px; line-height: 27px; color: var(--white); padding-left: 12px; white-space: nowrap; letter-spacing: 0.3px; }
  .footer-band strong { font-weight: 700; }
  .footer-band .current { color: var(--green); font-weight: 700; }

  .brand { position: absolute; left: 980px; top: 624px; display: flex; align-items: center; gap: 7px; }
  .brand .dot { width: 22px; height: 22px; border-radius: 50%; background: var(--green); }
  .brand .name { font-family: "Cabin", sans-serif; font-weight: 600; font-size: 14px; line-height: 15px; color: var(--green); letter-spacing: 0.8px; }
</style>
</head>
<body>
<div class="slide">

  <h1 class="title">Lorem ipsum dolor<br>sit amet adipiscing<br>elit sed diam</h1>

  <div class="legend-item legend-green">
    <span class="swatch"></span>
    <p>Lorem ipsum dolor sit amet,<br>consectetuer adipiscing eli.</p>
  </div>
  <div class="legend-item legend-white">
    <span class="swatch"></span>
    <p>Lorem ipsum dolor sit amet,<br>consectetuer adipiscing eli.</p>
  </div>

  <svg class="kpi-icon" width="60" height="60" viewBox="0 0 60 60" aria-hidden="true">
    <circle cx="30" cy="30" r="28" fill="none" stroke="var(--green)" stroke-width="2.6"/>
    <path d="M30 16 V42 M20 32 L30 42 L40 32" fill="none" stroke="var(--green)" stroke-width="2.6" stroke-linecap="round" stroke-linejoin="round"/>
  </svg>
  <div class="kpi-value">-25% Y/Y</div>
  <p class="kpi-note">Lorem ipsum dolor sit amet,<br>consectetuer adipiscing eli.</p>

  <div class="breadcrumb-bar"></div>
  <div class="breadcrumb">OTHER SLIDES &gt;&gt; CAPTIONED GRAPHIC &gt;&gt; LOREM IPSUM DOLOR</div>

  <svg class="chart" viewBox="0 0 1200 675" aria-label="Line chart comparing two series">
    <g stroke="var(--grid)" stroke-width="1.2">
      <line x1="595" y1="153" x2="1134" y2="153"/>
      <line x1="595" y1="199" x2="1134" y2="199"/>
      <line x1="595" y1="247" x2="1134" y2="247"/>
      <line x1="595" y1="294" x2="1134" y2="294"/>
      <line x1="595" y1="342" x2="1134" y2="342"/>
    </g>
    <line x1="595" y1="142" x2="595" y2="396" stroke="var(--grey)" stroke-width="1.6"/>
    <line x1="595" y1="395.5" x2="1134" y2="395.5" stroke="var(--grey)" stroke-width="1.6"/>

    <g text-anchor="end">
      <text x="586" y="158">1000</text>
      <text x="586" y="205">700</text>
      <text x="586" y="252">500</text>
      <text x="586" y="300">300</text>
      <text x="586" y="347">100</text>
      <text x="586" y="398">0</text>
    </g>
    <g text-anchor="middle">
      <text x="622" y="427">100</text>
      <text x="670" y="427">200</text>
      <text x="719" y="427">300</text>
      <text x="768" y="427">400</text>
      <text x="816" y="427">500</text>
      <text x="865" y="427">600</text>
      <text x="914" y="427">600</text>
      <text x="962" y="427">700</text>
      <text x="1011" y="427">800</text>
      <text x="1060" y="427">900</text>
      <text x="1113" y="427">1000</text>
    </g>

    <polyline fill="none" stroke="var(--grey)" stroke-width="2.4" stroke-linejoin="round"
      points="623,338 665,370 718,293 767,340 819,293 913,293 964,193 1014,343 1060,341 1135,154"/>
    <g fill="var(--grey)">
      <circle cx="623" cy="338" r="5"/><circle cx="665" cy="370" r="5"/><circle cx="718" cy="293" r="5"/>
      <circle cx="767" cy="340" r="5"/><circle cx="819" cy="293" r="5"/><circle cx="913" cy="293" r="5"/>
      <circle cx="964" cy="193" r="5"/><circle cx="1014" cy="343" r="5"/><circle cx="1060" cy="341" r="5"/>
      <circle cx="1135" cy="154" r="5"/>
    </g>

    <polyline fill="none" stroke="var(--green-dim)" stroke-width="2.4" stroke-linejoin="round"
      points="618,293 664,293 718,199 768,390 819,248 875,248 914,339 964,339 1015,293 1060,342 1134,294"/>
    <g fill="var(--green-dim)">
      <circle cx="618" cy="293" r="5"/><circle cx="664" cy="293" r="5"/><circle cx="718" cy="199" r="5"/>
      <circle cx="768" cy="390" r="5"/><circle cx="819" cy="248" r="5"/><circle cx="875" cy="248" r="5"/>
      <circle cx="914" cy="339" r="5"/><circle cx="964" cy="339" r="5"/><circle cx="1015" cy="293" r="5"/>
      <circle cx="1060" cy="342" r="5"/>
    </g>
  </svg>

  <div class="divider"></div>

  <div class="stat" style="left:58px">
    <div class="figure">-36</div>
    <div class="badge">
      <svg width="24" height="24" viewBox="0 0 24 24" fill="none" stroke="#1b1b1b" stroke-width="1.6" stroke-linecap="round" stroke-linejoin="round" aria-hidden="true">
        <path d="M12 3 A9 9 0 1 1 4.2 7.5"/><path d="M10 2.5 V10 H2.6 A7.5 7.5 0 0 1 10 2.5 Z"/>
      </svg>
    </div>
    <span class="rule"></span>
    <p>Lorem ipsum dolor situ amet,<br>consecteu adipiscing elit, sed<br>diam nonummy nibhas euism<br>utinci dunt ut laoreet.</p>
  </div>

  <div class="stat" style="left:339px">
    <div class="figure">6m</div>
    <div class="badge">
      <svg width="24" height="24" viewBox="0 0 24 24" fill="none" stroke="#1b1b1b" stroke-width="1.6" stroke-linecap="round" stroke-linejoin="round" aria-hidden="true">
        <path d="M3 11 L12 3 L21 11"/><path d="M5.5 9 V21 H18.5 V9"/><path d="M10 21 V14 H14 V21"/>
      </svg>
    </div>
    <span class="rule"></span>
    <p>Lorem ipsum dolor situ amet,<br>consecteu adipiscing elit, sed<br>diam nonummy nibhas euism<br>utinci dunt ut laoreet.</p>
  </div>

  <div class="stat" style="left:619px">
    <div class="figure">&lt;5%</div>
    <div class="badge">
      <svg width="24" height="24" viewBox="0 0 24 24" fill="none" stroke="#1b1b1b" stroke-width="1.6" stroke-linecap="round" stroke-linejoin="round" aria-hidden="true">
        <path d="M9 15 L6 12 C9 6 14 3 21 3 C21 10 18 15 12 18 Z"/><circle cx="15" cy="9" r="1.8"/><path d="M6 12 L3 12 L6 8 L9 8"/><path d="M12 18 L12 21 L16 18 L16 15"/><path d="M6 18 L3 21"/>
      </svg>
    </div>
    <span class="rule"></span>
    <p>Lorem ipsum dolor situ amet,<br>consecteu adipiscing elit, sed<br>diam nonummy nibhas euism<br>utinci dunt ut laoreet.</p>
  </div>

  <div class="stat" style="left:899px">
    <div class="figure">~2k</div>
    <div class="badge">
      <svg width="26" height="24" viewBox="0 0 26 24" fill="none" stroke="#1b1b1b" stroke-width="1.6" stroke-linecap="round" stroke-linejoin="round" aria-hidden="true">
        <path d="M8 18 H6.5 A4.5 4.5 0 0 1 6.5 9 A6 6 0 0 1 18 8 A4.5 4.5 0 0 1 19.5 18 H18"/><path d="M13 21 V12 M9.5 15 L13 11.5 L16.5 15"/>
      </svg>
    </div>
    <span class="rule"></span>
    <p>Lorem ipsum dolor situ amet,<br>consecteu adipiscing elit, sed<br>diam nonummy nibhas euism<br>utinci dunt ut laoreet.</p>
  </div>

  <div class="footer-num">10</div>
  <div class="footer-band">SMART MOBILITY &amp; KLO &gt;&gt; <strong>OTHER SLIDES</strong> &gt;&gt; <span class="current">DARK CAPTIONED GRAPHIC</span></div>

  <div class="brand">
    <span class="dot"></span>
    <span class="name">PLUMRIDGE<br>ADVISORS</span>
  </div>

</div>
</body>
</html>
```